Breezeway Climate Business Card Design

Design new, 2 sides, business cards for a residential and light commercial heating, air conditioning contractor.

Target Market(s)

Homeowners, small businesses

Industry/Entity Type

Business

Contact Information for Business Card

Dominic Vasquerelli
Phone - 555-214-6837
Email
Address - PO box 618
Millbrook NJ 07999
Website - www.BreezewayClimateLLC.example

Requirements
Must have
• logo, company colors, standard size with no die cut, so I can use printhaven

```html
<!DOCTYPE html>
<html lang="en">
<head>
<meta charset="utf-8">
<title>Breezeway Climate – Business Card</title>
<link href="https://fonts.googleapis.com/css2?family=Raleway:wght@300;400;600;800&display=swap" rel="stylesheet">
<style>
  :root {
    --page: #e8e4df;
    --ink: #0a0a0a;
    --crimson: #8e1c2b;
    --glow: #6a1a12;
    --gold: #e9d98f;
    --white: #ffffff;
    --grey-text: #7a7a7a;
    --light-text: #d8d8d8;
    --orange: #f08a24;
  }
  * { box-sizing: border-box; margin: 0; padding: 0; }
  html, body { width: 1200px; height: 913px; overflow: hidden; background: var(--page); }
  body { font-family: "Raleway", sans-serif; position: relative; }

  .card {
    position: absolute;
    left: 290px;
    width: 620px;
    height: 354px;
    border-radius: 4px;
    overflow: hidden;
    box-shadow: 0 8px 22px rgba(0,0,0,.28);
  }
  .card--front {
    top: 60px;
    background: radial-gradient(ellipse 55% 60% at 50% 50%, var(--glow) 0%, #3a0e0a 45%, var(--ink) 85%);
    display: flex; align-items: center; justify-content: center;
  }
  .front-name {
    font-weight: 800;
    font-size: 46px;
    letter-spacing: 2px;
    color: var(--gold);
    text-transform: uppercase;
  }

  .card--back { top: 493px; background: var(--ink); }
  .back-wave { position: absolute; inset: 0; width: 100%; height: 100%; }

  .contact {
    position: absolute; left: 38px; top: 46px; width: 320px;
  }
  .contact-name {
    font-size: 24px; color: var(--white); font-weight: 800;
    letter-spacing: .5px; padding-bottom: 9px;
    border-bottom: 1px solid #555;
    white-space: nowrap;
  }
  .contact-name .first { color: var(--gold); font-weight: 400; }
  .contact-list { list-style: none; margin-top: 11px; }
  .contact-list li {
    display: flex; align-items: center; gap: 10px;
    color: var(--light-text); font-size: 14px; font-weight: 400;
    margin-bottom: 7px; white-space: nowrap;
  }
  .contact-list svg { width: 14px; height: 14px; flex: none; }

  .back-brand {
    position: absolute; right: 24px; top: 126px;
    font-weight: 800; font-size: 16px; color: var(--crimson);
    text-transform: uppercase; letter-spacing: 1px;
    white-space: nowrap;
  }
  .address {
    position: absolute; right: 56px; top: 184px;
    color: var(--grey-text); font-size: 18px; font-weight: 400; line-height: 1.3;
    white-space: nowrap;
  }
  .address .home-icon { width: 18px; height: 18px; display: block; margin: 0 0 6px 96px; }
</style>
</head>
<body>

<section class="card card--front">
  <p class="front-name">Breezeway Climate</p>
</section>

<section class="card card--back">
  <svg class="back-wave" viewBox="0 0 620 354" preserveAspectRatio="none">
    <path d="M0,300 C260,300 330,70 620,20 L620,354 L0,354 Z" fill="var(--crimson)"/>
    <path d="M0,314 C260,314 330,84 620,34 L620,354 L0,354 Z" fill="var(--white)"/>
  </svg>

  <div class="contact">
    <p class="contact-name"><span class="first">Dominic</span> VASQUERELLI</p>
    <ul class="contact-list">
      <li>
        <svg viewBox="0 0 16 16"><circle cx="8" cy="8" r="7" fill="none" stroke="#888" stroke-width="1.2"/><path d="M5.5 4.5l1.5 1.5-1 1a5 5 0 0 0 3 3l1-1 1.5 1.5-1 1C7.5 12 4 8.5 4.5 5.5z" fill="#888"/></svg>
        555-214-6837
      </li>
      <li>
        <svg viewBox="0 0 16 16"><circle cx="8" cy="8" r="7" fill="none" stroke="#888" stroke-width="1.2"/><path d="M1 8h14M8 1c3 3 3 11 0 14M8 1c-3 3-3 11 0 14" fill="none" stroke="#888" stroke-width="1"/></svg>
        www.BreezewayClimateLLC.example
      </li>
    </ul>
  </div>

  <p class="back-brand">Breezeway Climate</p>

  <div class="address">
    <svg class="home-icon" viewBox="0 0 20 20"><rect x="1" y="1" width="18" height="18" fill="none" stroke="var(--orange)" stroke-width="1.6"/><path d="M5 10l5-4.5 5 4.5M7 9v6h6V9" fill="none" stroke="var(--orange)" stroke-width="1.6"/></svg>
    PO box 618<br>Millbrook NJ 07999
  </div>
</section>

</body>
</html>
```